Korvane Sky Works, LLC - Business Card

I currently have a drone business that specializes in aerial photography, thermal image inspections, deer recovery, search and rescue, custom agricultural applications. i will attach my current business card as well as some logos to incorporate for a new up to date business card
Updates

Designs look the same

Sick

Target Market(s)

farmers, hunters

Contact Information for Business Card

name address phone number (as existing card i attached)

Requirements
Must have
• im good with existing business card, but would like an agricultural twist

```html
<!DOCTYPE html>
<html lang="en">
<head>
<meta charset="utf-8">
<title>Korvane Sky Works, LLC – Business Card</title>
<link rel="stylesheet" href="https://fonts.googleapis.com/css2?family=Arimo:wght@400;700&display=swap">
<style>
  :root {
    --bg: #d9dadb;
    --green-light: #4e9624;
    --green-mid: #2f7d17;
    --green-dark: #17620e;
    --accent: #3a9a1d;
    --paper: #ffffff;
    --ink: #2a2a2a;
    --on-green: #ffffff;
  }
  * { box-sizing: border-box; margin: 0; padding: 0; }
  html, body { width: 1200px; height: 800px; overflow: hidden; }
  body {
    background: var(--bg);
    font-family: "Arimo", Arial, sans-serif;
    display: flex;
    align-items: center;
    justify-content: center;
    gap: 40px;
  }
  .card {
    width: 525px;
    height: 300px;
    border-radius: 22px;
    position: relative;
    box-shadow: 0 6px 18px rgba(0,0,0,0.18);
    overflow: hidden;
  }
  /* Front: contact side */
  .card--contact {
    background: radial-gradient(ellipse at 50% 45%, var(--green-light) 0%, var(--green-mid) 45%, var(--green-dark) 100%);
    color: var(--on-green);
  }
  .contact-block {
    position: absolute;
    left: 120px;
    top: 96px;
  }
  .holder {
    font-size: 22px;
    font-weight: 700;
    margin-left: 56px;
    margin-bottom: 14px;
  }
  .holder .role { font-weight: 400; font-size: 15px; }
  .details { display: flex; align-items: stretch; }
  .address {
    text-align: right;
    font-size: 14px;
    line-height: 1.45;
    padding-right: 14px;
    width: 150px;
  }
  .divider { width: 1px; background: rgba(255,255,255,0.75); }
  .lines {
    font-size: 13.5px;
    line-height: 1.5;
    padding-left: 14px;
  }
  .lines b { font-weight: 700; display: inline-block; width: 18px; }

  /* Back: brand side */
  .card--brand { background: var(--paper); color: var(--ink); }
  .brand {
    position: absolute;
    top: 70px;
    left: 0; right: 0;
    display: flex;
    align-items: center;
    justify-content: center;
    gap: 12px;
  }
  .brand-dot {
    width: 30px; height: 30px;
    border-radius: 50%;
    background: var(--accent);
  }
  .brand-name {
    font-size: 40px;
    font-weight: 700;
    color: var(--accent);
    letter-spacing: 1px;
  }
  .services {
    position: absolute;
    bottom: 34px;
    left: 0; right: 0;
    display: flex;
    justify-content: center;
    align-items: center;
    gap: 8px;
    font-size: 12.5px;
    list-style: none;
  }
  .services li { display: flex; align-items: center; gap: 8px; }
  .services li + li::before {
    content: "";
    width: 7px; height: 7px;
    border-radius: 50%;
    background: var(--accent);
  }
</style>
</head>
<body>
  <section class="card card--contact" aria-label="Contact side">
    <div class="contact-block">
      <p class="holder">Dorian Vaskel / <span class="role">Owner</span></p>
      <div class="details">
        <address class="address" style="font-style:normal">212 W. Orchard Ave.<br>Marlow<br>OH 45000</address>
        <span class="divider"></span>
        <p class="lines">
          <b>P</b>: 555-014-2290<br>
          <b>E</b>: korvaneskyworks@mailbox.com<br>
          <b>W</b>: www.korvaneskyworks.com
        </p>
      </div>
    </div>
  </section>

  <section class="card card--brand" aria-label="Brand side">
    <div class="brand">
      <span class="brand-dot"></span>
      <span class="brand-name">Korvane</span>
    </div>
    <ul class="services">
      <li>Thermal Image Inspections</li>
      <li>Deer Recovery</li>
      <li>Search&amp; Rescue</li>
      <li>Real Estate Photography</li>
    </ul>
  </section>
</body>
</html>
```